Logo Tweak & Full Set of Stationery

We need a redesign / tweaking of Logo for rebranding of our company. We are Australia's largest installer of commercial fencing and high security infrastructure. We also have divisions in security and civil works (infrastrucuture).

We would like to see designs that incorporate black, white & blue. Revamp of current Diamond Logo (including HU) would be ideal but open to all ideas.

Design needs to portray a highly professional & corporate image.

Required:
- Tweak / Redesign of Logo
- Letterhead
- email Signature
- Business Cards
- Presentation Folder

Address fields should be interchangeable to accomodate multiple locations.

Website: www.harwickunion.com.au
Updates

Due to short turn around time for project - Fee increased to $500 AUD Guaranteed

Thanks

Designs are looking good
I have emailed those submitted thus far to the board to start short listing.

Please do not take offence if your design is eliminated as part of this process  - there are so many great concepts and if is difficult to pick between them.

Thanks
Desmond

Target Market(s)

Tier 1 / 2 Builders (ie.. Brant Vale Peter Ashdown) and Government related bodies

Industry/Entity Type

Security

Requirements
Must have
• Company Name: Harwick Union

Tag Line: Fencing * Security * Civil

Logo

```html
<!DOCTYPE html>
<html lang="en">
<head>
<meta charset="utf-8">
<title>Harwick Union – Stationery Set</title>
<link rel="stylesheet" href="https://fonts.googleapis.com/css2?family=Michroma&family=Arimo:wght@400;700&display=swap">
<style>
  :root {
    --stage: #0e0e0e;
    --stage-glow: #2a2a2a;
    --paper: #ffffff;
    --frame-grey: #b3b4b6;
    --blue-deep: #0a1c9a;
    --blue-bright: #1d6cf2;
    --ink: #111111;
    --ink-soft: #3a3a3a;
    --tag-blue: #1a5fe0;
    --sand: #c6b59a;
    --pearl: #e4ded2;
    --muted: #9a9a9a;
  }
  * { margin: 0; padding: 0; box-sizing: border-box; }
  html, body { width: 1200px; height: 900px; overflow: hidden; }
  body {
    background: radial-gradient(ellipse at 50% 45%, var(--stage-glow), var(--stage) 75%);
    font-family: "Arimo", Arial, sans-serif;
    position: relative;
  }
  .piece { position: absolute; }
  .piece > svg { position: absolute; inset: 0; width: 100%; height: 100%; display: block; }

  .brand { position: absolute; display: flex; align-items: flex-start; gap: 8px; }
  .brand-dot { border-radius: 50%; background: var(--blue-deep); flex: none; }
  .brand-name {
    font-family: "Michroma", "Arial Black", sans-serif;
    color: var(--ink); letter-spacing: 0.12em; white-space: nowrap; line-height: 1;
  }
  .brand-tag { color: var(--tag-blue); white-space: nowrap; line-height: 1; margin-top: 5px; letter-spacing: 0.02em; }

  /* Letterhead */
  .letterhead { left: 50px; top: 95px; width: 503px; height: 695px; }
  .letterhead .brand { left: 58px; top: 70px; }
  .letterhead .brand-dot { width: 50px; height: 50px; }
  .letterhead .brand-name { font-size: 13px; margin-top: 14px; }
  .letterhead .brand-tag { font-size: 8px; }
  .side-label {
    position: absolute; left: 430px; top: 328px; transform: rotate(-90deg); transform-origin: left top;
    font-weight: 700; font-size: 9px; color: var(--muted); white-space: nowrap;
  }
  .side-web {
    position: absolute; left: 431px; top: 495px; transform: rotate(-90deg); transform-origin: left top;
    font-size: 6px; color: #d8d8d8; white-space: nowrap;
  }
  .letterhead .web { position: absolute; left: 372px; top: 647px; font-size: 9px; color: var(--ink-soft); }

  /* Compliments slip */
  .slip { left: 612px; top: 95px; width: 203px; height: 221px; }
  .slip .brand { left: 18px; top: 26px; gap: 5px; }
  .slip .brand-dot { width: 28px; height: 28px; }
  .slip .brand-name { font-size: 7.5px; margin-top: 8px; }
  .slip .brand-tag { font-size: 5px; margin-top: 3px; }
  .slip .contact { position: absolute; left: 0; right: 0; top: 190px; text-align: center; font-size: 5.6px; line-height: 1.55; color: var(--ink-soft); }

  /* Business card */
  .card { left: 602px; top: 352px; width: 223px; height: 120px; }
  .card .brand { left: 10px; top: 50px; gap: 4px; }
  .card .brand-dot { width: 24px; height: 24px; }
  .card .brand-name { font-size: 5.2px; letter-spacing: 0.06em; margin-top: 7px; }
  .card .brand-tag { font-size: 4.5px; margin-top: 3px; }
  .card .person { position: absolute; right: 26px; top: 36px; text-align: right; font-size: 6.5px; line-height: 1.6; color: var(--sand); }
  .card .details { position: absolute; left: 120px; top: 57px; font-size: 5.6px; line-height: 1.45; color: var(--sand); }

  /* Disc */
  .disc { left: 870px; top: 141px; width: 276px; height: 276px; }
  .disc .brand { left: 78px; top: 57px; gap: 6px; }
  .disc .brand-dot { width: 34px; height: 34px; }
  .disc .brand-name { font-size: 8.5px; margin-top: 9px; }
  .disc .brand-tag { font-size: 5.5px; margin-top: 3px; }
  .disc .list { position: absolute; top: 112px; font-size: 6.5px; line-height: 8.5px; color: var(--sand); }
  .disc .list-left { left: 36px; }
  .disc .list-right { left: 192px; }
  .disc .title { position: absolute; left: 0; right: 0; top: 196px; text-align: center; font-size: 8.5px; color: var(--sand); font-weight: 700; }
  .disc .web { position: absolute; left: 0; right: 0; top: 207px; text-align: center; font-size: 7px; color: var(--sand); }

  /* Folder */
  .folder { left: 598px; top: 509px; width: 560px; height: 283px; }
  .folder .back-copy { position: absolute; left: 23px; top: 233px; color: #6d6d6d; }
  .folder .back-copy h2 { font-size: 8.5px; font-weight: 400; margin-bottom: 3px; }
  .folder .back-copy p { font-size: 6px; line-height: 1.35; }
  .folder .brand { left: 308px; top: 201px; gap: 6px; }
  .folder .brand-dot { width: 36px; height: 36px; }
  .folder .brand-name { font-size: 10px; margin-top: 10px; }
  .folder .brand-tag { font-size: 6px; margin-top: 4px; }
</style>
</head>
<body>

<!-- Letterhead -->
<section class="piece letterhead">
  <svg viewBox="0 0 503 695" preserveAspectRatio="none">
    <defs>
      <linearGradient id="lh-blue" x1="0" y1="0" x2="1" y2="0">
        <stop offset="0" stop-color="#0a1c9a"/><stop offset="0.6" stop-color="#1d6cf2"/><stop offset="1" stop-color="#0a1c9a"/>
      </linearGradient>
    </defs>
    <rect width="503" height="695" fill="#b3b4b6"/>
    <rect x="7" y="0" width="496" height="686" fill="#ffffff"/>
    <path d="M140,0 Q380,22 503,92 L503,0 Z" fill="#b3b4b6"/>
    <path d="M160,0 Q380,16 503,82 L503,0 Z" fill="url(#lh-blue)"/>
    <path d="M283,8 L496,8 L496,70" fill="none" stroke="#ffffff" stroke-width="0.8"/>
    <path d="M0,605 Q150,680 390,695 L0,695 Z" fill="#b3b4b6"/>
    <path d="M0,614 Q150,688 360,695 L0,695 Z" fill="url(#lh-blue)"/>
    <path d="M8,622 L8,687 L220,687" fill="none" stroke="#ffffff" stroke-width="0.8"/>
    <circle cx="352" cy="651" r="11" fill="#e4ded2"/>
  </svg>
  <div class="brand">
    <span class="brand-dot"></span>
    <div><div class="brand-name">HARWICK UNION</div><div class="brand-tag">Fencing * Security * Civil</div></div>
  </div>
  <div class="side-label">Sample Text</div>
  <div class="side-web">www.yourwebsite.com</div>
  <div class="web">www.yourwebsite.com</div>
</section>

<!-- Compliments slip -->
<section class="piece slip">
  <svg viewBox="0 0 203 221" preserveAspectRatio="none">
    <defs>
      <linearGradient id="sl-blue" x1="0" y1="0" x2="1" y2="0">
        <stop offset="0" stop-color="#1d6cf2"/><stop offset="1" stop-color="#0a1c9a"/>
      </linearGradient>
    </defs>
    <rect width="203" height="221" fill="#ffffff"/>
    <path d="M0,0 L203,0 L203,50 Q130,5 0,5 Z" fill="#b3b4b6"/>
    <path d="M110,0 L203,0 L203,42 Q170,10 110,0 Z" fill="url(#sl-blue)"/>
  </svg>
  <div class="brand">
    <span class="brand-dot"></span>
    <div><div class="brand-name">HARWICK UNION</div><div class="brand-tag">Fencing * Security * Civil</div></div>
  </div>
  <div class="contact">
    Address: Text text text text text text text text text text text<br>
    Ph.:+000 00 000 00 00,+000 00 000 00 00,fax.:+000 00 000 00 00<br>
    www.yourwebsite.com; e-mail: office@yourwebsite.com
  </div>
</section>

<!-- Business card -->
<section class="piece card">
  <svg viewBox="0 0 223 120" preserveAspectRatio="none">
    <defs>
      <linearGradient id="bc-blue" x1="0" y1="0" x2="1" y2="0">
        <stop offset="0" stop-color="#0a1c9a"/><stop offset="0.5" stop-color="#1d6cf2"/><stop offset="1" stop-color="#0a1c9a"/>
      </linearGradient>
    </defs>
    <rect width="223" height="120" fill="#ffffff"/>
    <path d="M90,0 L223,0 L223,38 Q180,8 90,0 Z" fill="#b3b4b6"/>
    <path d="M0,80 Q60,112 160,120 L0,120 Z" fill="#b3b4b6"/>
    <path d="M0,88 Q50,116 140,120 L0,120 Z" fill="url(#bc-blue)"/>
  </svg>
  <div class="brand">
    <span class="brand-dot"></span>
    <div><div class="brand-name">HARWICK UNION</div><div class="brand-tag">Fencing * Security * Civil</div></div>
  </div>
  <div class="person">First and Last Name<br>Post</div>
  <div class="details">
    Address: Text text text<br>text text text text text<br>Tel.: +00 000 000 00 00<br>Fax.: +00 000 000 00 00<br>office@yourwebsite.com
  </div>
</section>

<!-- Disc -->
<section class="piece disc">
  <svg viewBox="0 0 276 276">
    <defs>
      <clipPath id="disc-clip"><circle cx="138" cy="138" r="137"/></clipPath>
      <linearGradient id="cd-blue" x1="0" y1="1" x2="1" y2="0">
        <stop offset="0" stop-color="#0a1c9a"/><stop offset="0.6" stop-color="#1d6cf2"/><stop offset="1" stop-color="#0a1c9a"/>
      </linearGradient>
      <radialGradient id="cd-hub" cx="0.5" cy="0.5" r="0.5">
        <stop offset="0" stop-color="#222222"/><stop offset="1" stop-color="#050505"/>
      </radialGradient>
    </defs>
    <g clip-path="url(#disc-clip)">
      <rect width="276" height="276" fill="#ffffff"/>
      <path d="M0,0 L190,0 Q90,30 0,110 Z" fill="#b3b4b6"/>
      <path d="M190,0 Q90,30 0,110" fill="none" stroke="#d9c9a6" stroke-width="1"/>
      <path d="M70,276 Q200,250 276,180 L276,276 Z" fill="url(#cd-blue)"/>
    </g>
    <circle cx="138" cy="138" r="137" fill="none" stroke="#2a2a2a" stroke-width="2"/>
    <circle cx="138" cy="141" r="44" fill="url(#cd-hub)"/>
    <circle cx="138" cy="141" r="22" fill="#1a1a1a" stroke="#5a5a5a" stroke-width="2"/>
  </svg>
  <div class="brand">
    <span class="brand-dot"></span>
    <div><div class="brand-name">HARWICK UNION</div><div class="brand-tag">Fencing * Security * Civil</div></div>
  </div>
  <div class="list list-left">sample text ·<br>sample text ·<br>sample text ·<br>sample text ·<br>sample text ·<br>sample text ·<br>sample text ·</div>
  <div class="list list-right">· sample text<br>· sample text<br>· sample text<br>· sample text<br>· sample text<br>· sample text<br>· sample text</div>
  <div class="title">Sample Text</div>
  <div class="web">www.yourwebsite.com</div>
</section>

<!-- Presentation folder -->
<section class="piece folder">
  <svg viewBox="0 0 560 283" preserveAspectRatio="none">
    <defs>
      <radialGradient id="fd-blue" cx="0.45" cy="0.5" r="0.6">
        <stop offset="0" stop-color="#1d7cff"/><stop offset="1" stop-color="#0a1c9a"/>
      </radialGradient>
      <linearGradient id="fd-band" x1="0" y1="0" x2="1" y2="0">
        <stop offset="0" stop-color="#0a1c9a"/><stop offset="0.6" stop-color="#1d6cf2"/><stop offset="1" stop-color="#0a1c9a"/>
      </linearGradient>
    </defs>
    <rect x="0" y="0" width="280" height="283" fill="#ffffff"/>
    <path d="M0,60 Q110,110 165,283 L0,283 Z" fill="#b3b4b6"/>
    <path d="M133,0 L280,0 L280,185 Q160,120 133,0 Z" fill="url(#fd-blue)"/>
    <circle cx="169" cy="170" r="10" fill="#e4ded2"/>
    <circle cx="180" cy="201" r="6" fill="#e4ded2"/>
    <rect x="280" y="0" width="280" height="283" fill="#b3b4b6"/>
    <rect x="281" y="8" width="272" height="275" fill="#ffffff"/>
    <path d="M360,0 Q480,4 560,45 L560,0 Z" fill="#b3b4b6"/>
    <path d="M380,0 Q490,6 553,36 L553,0 Z" fill="url(#fd-band)"/>
    <path d="M281,246 Q380,280 460,283 L281,283 Z" fill="#b3b4b6"/>
    <path d="M281,252 Q360,282 430,283 L281,283 Z" fill="url(#fd-band)"/>
  </svg>
  <div class="back-copy">
    <h2>SAMPLE TEXT</h2>
    <p>sample text sample text sample text sample text<br>sample text sample text sample text sample text</p>
  </div>
  <div class="brand">
    <span class="brand-dot"></span>
    <div><div class="brand-name">HARWICK UNION</div><div class="brand-tag">Fencing * Security * Civil</div></div>
  </div>
</section>

</body>
</html>
```